high end kitchens , needing new logo and business card design .

im looking a very simple looking design but classy that will stand out , i would like the design to be in the colours black , silver , gold and grey , although all colours dont need to be used in design , back of card to have name on it colin fetterby , address and phone number and website address , maybe fb logo . adrress is 27 moorgate row , newtownards , bt41 2qd , 07718492265 , front of the card im open to design , back of card very simple i will want it matt black with silver writing , writing doesnt need to be that big

Target Market(s)

people with kitchen projects .

Industry/Entity Type

Interior Design

Contact Information for Business Card

front of business card hc on it with maybe harbor cabinets under it wrote smaller , maybe the card to be mate black with the writing in a gloss black or silver

Logo Text

hc . harbor cabinets

Font styles to use
Sans Serif
Script

Colors
1b1b1b
919191
f6f6f6
848484
ffc214
ec1f27

Requirements
Must have
• clean and simple , not too fussy ,
Nice to have
• n/a
Should not have
• n/a

```html
<!DOCTYPE html>
<html lang="en">
<head>
<meta charset="utf-8">
<title>Harbor Cabinets – Business Card</title>
<link href="https://fonts.googleapis.com/css2?family=Montserrat:wght@300;400;600;700&display=swap" rel="stylesheet">
<style>
  :root {
    --backdrop: #cfcfd1;
    --card-black: #141414;
    --card-black-soft: #1c1c1c;
    --gold: #f2b61f;
    --gold-deep: #c99526;
    --bronze: #c58d37;
  }
  * { margin: 0; padding: 0; box-sizing: border-box; }
  html, body {
    width: 1198px; height: 1200px; overflow: hidden;
    background: var(--backdrop);
    font-family: "Montserrat", sans-serif;
  }
  .stage { position: relative; width: 1198px; height: 1200px; }
  .card {
    position: absolute; top: 451px; width: 522px; height: 298px;
    background: radial-gradient(ellipse at 40% 30%, var(--card-black-soft), var(--card-black) 70%);
    overflow: hidden;
  }
  .card--front { left: 64px; }
  .card--back { left: 612px; }

  .brand-square {
    position: absolute; left: 52px; top: 170px; width: 85px; height: 85px;
    border: 3px solid var(--gold-deep);
  }
  .brand-name {
    position: absolute; left: 147px; top: 227px;
    font-weight: 300; font-size: 22px; letter-spacing: 0.5px;
    color: var(--bronze); white-space: nowrap;
  }

  .gold-rule {
    position: absolute; left: 81px; top: 0; width: 6px; height: 100%;
    background: linear-gradient(180deg, var(--gold-deep), var(--gold), var(--gold-deep));
  }
  .name-first, .name-last {
    position: absolute; writing-mode: vertical-rl; transform: rotate(180deg);
    color: var(--gold); white-space: nowrap; line-height: 1;
  }
  .name-first { left: 31px; bottom: 45px; font-size: 23px; font-weight: 700; letter-spacing: 0.5px; }
  .name-last { left: 54px; bottom: 82px; font-size: 16px; font-weight: 400; letter-spacing: 1px; }

  .contact-list { position: absolute; left: 102px; top: 193px; list-style: none; }
  .contact-list li {
    display: flex; align-items: center; height: 20.5px;
    font-size: 11.5px; font-weight: 600; color: var(--gold); white-space: nowrap;
  }
  .contact-list svg { width: 9px; height: 9px; margin-right: 8px; flex: none; fill: var(--gold); }
</style>
</head>
<body>
<main class="stage">
  <section class="card card--front">
    <div class="brand-square"></div>
    <div class="brand-name">Harbor Cabinets</div>
  </section>

  <section class="card card--back">
    <div class="name-first">COLIN</div>
    <div class="name-last">FETTERBY</div>
    <div class="gold-rule"></div>
    <ul class="contact-list">
      <li><svg viewBox="0 0 10 10"><path d="M5 0a3.5 3.5 0 0 0-3.5 3.5C1.5 6 5 10 5 10s3.5-4 3.5-6.5A3.5 3.5 0 0 0 5 0zm0 5a1.4 1.4 0 1 1 0-2.8A1.4 1.4 0 0 1 5 5z"/></svg>27 Moorgate Row, Carrowdale BT41 2QD</li>
      <li><svg viewBox="0 0 10 10"><path d="M2 0.5l1.8 2.2-1 1.2a6 6 0 0 0 3.3 3.3l1.2-1L9.5 8l-1.3 1.5C4.5 9.5.5 5.5.5 1.8z"/></svg>+44 7718 492265</li>
      <li><svg viewBox="0 0 10 10"><path d="M0 2h10v1L5 6 0 3zM0 4.2l5 3 5-3V8.5H0z"/></svg>studio@harborcabinets.co.uk</li>
      <li><svg viewBox="0 0 10 10"><path fill="none" stroke="#f2b61f" stroke-width="1" d="M5 .5a4.5 4.5 0 1 0 0 9 4.5 4.5 0 0 0 0-9zM.5 5h9M5 .5c-2.4 2.5-2.4 6.5 0 9M5 .5c2.4 2.5 2.4 6.5 0 9"/></svg>www.harborcabinets.co.uk</li>
    </ul>
  </section>
</main>
</body>
</html>
```